Stage Design Company Business Card

We are looking to step up up our business card design for our team.

We are a Full service Design and Consultation company for Stage and TV with an emphasis in Theatrical Lighting.

We like our materials to be clean and modern with solid colors free of patterns and gradients. Our brand consists of 4 primary colors Purple, Black, Grey, and White. Provided is our Word Mark as well as our Symbol Logo.

We would like our cards to leave an impression beyond the information, show our attention to design and detail, and make our marks an easily recognized feature (together or apart) for our clients.

We need a warm approachable comfortable feel for some clients, and a professional flair for the board member type clients.

Attached are our brand elements, and our existing cards to give a sense of our style and a glipse at the information we provide on our cards.

Target Market(s)

broad client base from church leaders to high school teachers and architects.

Industry/Entity Type

Business

Contact Information for Business Card

We format our phone number with periods not parenthesis or dashes. Information will be edited for each of our team members, and team member specific cards are not part of this scope, but rather a template so to speak.

Font styles to use
Sans Serif

Colors
6b449b
ffffff
000000
333333
aaaaaa

Requirements
Must have
• Wordmark and logo mark present (does not need to exist on the same side of card)
• Brand Colors,
• Name, Phone, Email, Address.
• Unique choices that make someone stop and take a second look
Nice to have
• It would be nice to somehow convey what we DO, as our brand name does not lend itself to this, outside of an obvious tagline though.....
• social media if not crowded. all of our handles match (instagram, twitter, facebook)
Should not have
• "clipart"

```html
<!DOCTYPE html>
<html lang="en">
<head>
<meta charset="utf-8">
<title>Kessler Stageworks – Business Card</title>
<link href="https://fonts.googleapis.com/css2?family=Mulish:wght@400;700;800&display=swap" rel="stylesheet">
<style>
  :root {
    --backdrop: #161616;
    --paper: #fbf8f3;
    --purple: #3b2a6b;
    --ink: #000000;
    --grey: #aaaaaa;
    --soft-white: #e4def0;
  }
  html, body {
    margin: 0;
    width: 1200px;
    height: 1000px;
    overflow: hidden;
    background: var(--backdrop);
    font-family: "Mulish", Arial, sans-serif;
  }
  .stage {
    position: relative;
    width: 1200px;
    height: 1000px;
  }
  .card {
    position: absolute;
    top: 350px;
    width: 520px;
    height: 298px;
    box-sizing: border-box;
    overflow: hidden;
  }
  /* Front */
  .card-front {
    left: 50px;
    background: var(--paper);
    display: flex;
    flex-direction: column;
    align-items: center;
    justify-content: center;
  }
  .wordmark {
    margin: 0;
    font-weight: 800;
    font-size: 40px;
    letter-spacing: 26px;
    padding-left: 26px;
    color: var(--ink);
    line-height: 1;
  }
  .wordmark-sub {
    margin: 12px 0 0;
    font-weight: 400;
    font-size: 12px;
    letter-spacing: 15px;
    padding-left: 15px;
    color: var(--grey);
    text-transform: uppercase;
  }
  /* Back */
  .card-back {
    left: 630px;
    background: var(--purple);
  }
  .name-band {
    height: 72px;
    background: var(--paper);
    display: flex;
    align-items: flex-end;
    justify-content: space-between;
    padding: 0 26px 14px 30px;
    box-sizing: border-box;
  }
  .person-name {
    margin: 0 0 10px;
    font-weight: 800;
    font-size: 19px;
    color: var(--purple);
    align-self: flex-start;
    margin-top: 22px;
  }
  .social-handle {
    display: flex;
    align-items: center;
    gap: 8px;
    font-weight: 800;
    font-size: 13px;
    color: var(--purple);
    letter-spacing: 0.5px;
  }
  .social-handle .dot {
    width: 10px;
    height: 10px;
    border-radius: 50%;
    background: var(--purple);
  }
  .contact {
    position: absolute;
    left: 30px;
    top: 96px;
    margin: 0;
    font-style: normal;
    font-size: 13px;
    line-height: 1.3;
    color: var(--soft-white);
  }
  .contact p { margin: 0; }
  .contact .address { margin-top: 10px; }
  .symbol-stand-in {
    position: absolute;
    right: 26px;
    bottom: 32px;
    display: flex;
    align-items: center;
    gap: 8px;
    font-weight: 800;
    font-size: 15px;
    color: var(--paper);
    letter-spacing: 1px;
  }
  .symbol-stand-in .ring {
    width: 14px;
    height: 14px;
    border-radius: 50%;
    background: var(--paper);
  }
</style>
</head>
<body>
<main class="stage">
  <section class="card card-front" aria-label="Card front">
    <h1 class="wordmark">KESSLER</h1>
    <p class="wordmark-sub">Stageworks</p>
  </section>

  <section class="card card-back" aria-label="Card back">
    <header class="name-band">
      <h2 class="person-name">Mara L Quinn</h2>
      <div class="social-handle"><span class="dot"></span>KESSLER-SW</div>
    </header>
    <address class="contact">
      <p>800.555.0148</p>
      <p>mara@kessler-sw.com</p>
      <p>kessler-sw.com</p>
      <p class="address">52 N Elm St Tempe</p>
      <p>AZ 85281</p>
    </address>
    <div class="symbol-stand-in"><span class="ring"></span>KESSLER</div>
  </section>
</main>
</body>
</html>
```